Zielgruppe
Ich bin selbständiger Vertriebspartner der Firma LURADI (hochwertige Reinigungsprodukte), und für eine meiner Zielgruppen 'Hundebesitzer/Hundeschulen etc' möchte ich mit zwei Produkten (Glanz Helfer Lappen, Fußmatte) einen tollen Flyer.
Aufgabenstellung
Aufgrund von Markenrechtvorgaben sind z.B. Schreibweise, Farbe des Logos etc vorgeschrieben.
Designmäßig würde ich mich über einen 'Eyecatcher' :-) freuen. Der Flyer soll die 3 A's beinhalten... anders sein als andere :-), gerne auch hinsichtlich des Formates.

```html
<!DOCTYPE html>
<html lang="de">
<head>
<meta charset="utf-8">
<title>LURADI – Produkte für deinen Hund</title>
<link rel="stylesheet" href="https://fonts.googleapis.com/css2?family=Quicksand:wght@400;500;700&display=swap">
<style>
  :root{
    --stage:#e4e1cc;
    --yellow:#f6c619;
    --yellow-deep:#f1b914;
    --paper:#ffffff;
    --ink:#3a3322;
    --ink-soft:#4a4230;
    --fold:rgba(0,0,0,.06);
    --drawing:#f3f1ec;
  }
  *{box-sizing:border-box;margin:0;padding:0}
  html,body{width:1200px;height:865px;overflow:hidden;background:var(--stage)}
  body{font-family:"Quicksand",sans-serif;color:var(--ink)}
  .flyer{position:absolute;left:50px;top:42px;width:1100px;height:780px;overflow:hidden;box-shadow:0 10px 30px rgba(0,0,0,.12)}
  .flyer__shapes{position:absolute;inset:0}
  .panel-title{position:absolute;font-weight:500;font-size:30px;line-height:1.15;text-align:center}
  .title-left{left:40px;top:105px;width:287px}
  .title-right{left:760px;top:215px;width:300px;font-weight:700;font-size:29px}
  .body-copy{position:absolute;font-size:16px;line-height:1.4;font-weight:400;color:var(--ink-soft)}
  .copy-left{left:52px;top:215px;width:265px;text-align:center}
  .copy-mat{left:410px;top:268px;width:290px}
  .copy-mat strong{display:block;font-weight:700;color:var(--ink)}
  .sizes{position:absolute;left:410px;top:450px;width:290px;font-size:16px;line-height:1.5;color:var(--ink-soft)}
  .sizes li{list-style:none;display:flex}
  .sizes .size{width:40px}
  .sizes .dim{width:140px}
  .features{position:absolute;left:420px;top:625px;width:280px;font-size:13.5px;line-height:1.3;color:var(--ink-soft)}
  .features li{list-style:none;margin-bottom:12px}
  .brand{position:absolute;left:905px;top:610px;width:190px;display:flex;align-items:center;justify-content:center;gap:10px}
  .brand__dot{width:14px;height:14px;border-radius:50%;background:var(--yellow)}
  .brand__name{font-weight:500;font-size:30px;color:var(--ink);line-height:1}
</style>
</head>
<body>
<main class="flyer">
  <svg class="flyer__shapes" width="1100" height="780" viewBox="0 0 1100 780">
    <defs>
      <linearGradient id="dogCar" x1="0" y1="0" x2="1" y2="1">
        <stop offset="0" stop-color="#3a3a3c"/><stop offset=".5" stop-color="#5c5852"/><stop offset="1" stop-color="#7a6a56"/>
      </linearGradient>
      <linearGradient id="dogTowel" x1="0" y1="0" x2="1" y2="1">
        <stop offset="0" stop-color="#6d6a66"/><stop offset=".5" stop-color="#d8d0c2"/><stop offset="1" stop-color="#a47c5a"/>
      </linearGradient>
      <linearGradient id="matDoor" x1="0" y1="0" x2="0" y2="1">
        <stop offset="0" stop-color="#e6e4de"/><stop offset=".45" stop-color="#c49c74"/><stop offset="1" stop-color="#6b5a4c"/>
      </linearGradient>
    </defs>
    <rect class="panel-bg" width="1100" height="780" fill="var(--yellow)"/>
    <rect class="panel-bg-left" width="367" height="780" fill="var(--yellow-deep)" opacity=".35"/>
    <path class="white-band" d="M395 780 L395 640 Q395 603 440 600 L900 570 Q960 560 1000 520 L1100 430 L1100 780 Z" fill="var(--paper)"/>
    <line x1="367" y1="0" x2="367" y2="780" stroke="var(--fold)" stroke-width="2"/>
    <line x1="733" y1="0" x2="733" y2="780" stroke="var(--fold)" stroke-width="2"/>

    <circle cx="220" cy="730" r="200" fill="var(--paper)"/>
    <circle cx="220" cy="730" r="190" fill="url(#dogCar)" role="img" aria-label="Foto: weißer Hund sitzt auf einer Fußmatte im Kofferraum eines Autos"/>

    <rect x="440" y="35" width="230" height="210" fill="var(--drawing)" role="img" aria-label="Technische Zeichnung: Fußmatten in den Größen S, M und L übereinander"/>

    <circle cx="930" cy="-10" r="170" fill="var(--paper)"/>
    <circle cx="930" cy="-10" r="160" fill="url(#dogTowel)" role="img" aria-label="Foto: Hund liegt mit einem Reinigungstuch auf dem Autositz"/>

    <circle cx="850" cy="500" r="115" fill="var(--paper)"/>
    <circle cx="850" cy="500" r="106" fill="url(#matDoor)" role="img" aria-label="Foto: Kind und Hund auf einer Fußmatte an der Haustür"/>
  </svg>

  <h2 class="panel-title title-left">Schmutz &amp; Nässe draußen</h2>
  <p class="body-copy copy-left">Es gibt Fußmatten mit lustigen Sprüchen, Fußmatten in allen Formen und Farben und es gibt die LURADI Fußmatte – und nur die hält den Schmutz wirklich fest und ist immer wieder waschbar.</p>

  <p class="body-copy copy-mat"><strong>Fußmatte</strong>Damit bleibt der Schmutz garantiert draußen. Durch die einzigartige Borstenstruktur bietet die Fußmatte eine besonders hohe Schmutz- und Wasseraufnahme. Dabei ist sie enorm flach und passt unter fast jede Haustür.</p>
  <ul class="sizes">
    <li><span class="size">S</span><span class="dim">62 x 39 cm</span><span>36,90 €</span></li>
    <li><span class="size">M</span><span class="dim">73 x 52 cm</span><span>54,90 €</span></li>
    <li><span class="size">L</span><span class="dim">122 x 79 cm</span><span>134,90 €</span></li>
  </ul>
  <ul class="features">
    <li>Hohe Schmutz- und Wasseraufnahme</li>
    <li>Maschinenwaschbar bis 30 Grad C (Schonwäsche)</li>
    <li>Besonders rutschfest</li>
    <li>Extraflach</li>
  </ul>

  <h1 class="panel-title title-right">Tolle hochwertige Produkte für deinen Hund</h1>
  <div class="brand">
    <span class="brand__dot"></span>
    <span class="brand__name">LURADI</span>
  </div>
</main>
</body>
</html>
```